environmentalist needs a bumper sticker design

The bumper sticker should say, "There is no Planet B."

thank you for the designs so far. Some have asked for more direction of my thinking. You've probably heard people talk of "Plan A" and "Plan B" when they want to consider alternatives. "There is no Planet B" reminds us that there are no alternatives. The question is, how best to encourage people to act? Research indicates that making people fearful is less effective (although certainly we have plenty to fear). It is more effective to stir emotions of caring and attachment. For example, designs that show the earth as a beautiful planet, or aspects of the earth (e.g., trees and mountains or whatever) remind us of what we love and want to care for.

```html
<!DOCTYPE html>
<html lang="en">
<head>
<meta charset="utf-8">
<title>There is NO Planet B — Bumper Sticker</title>
<link rel="stylesheet" href="https://fonts.googleapis.com/css2?family=Poppins:wght@700&display=swap">
<style>
  :root {
    --canvas-grey: #d7d7d7;
    --sticker-deep: #04381f;
    --sticker-mid: #0a8a45;
    --sticker-light: #26b067;
    --text-white: #ffffff;
    --globe-light: #6fc23a;
    --globe-dark: #0b4a16;
    --ring-gold: #f4d23a;
  }
  html, body {
    margin: 0;
    padding: 0;
    width: 1200px;
    height: 1000px;
    overflow: hidden;
    background: var(--canvas-grey);
  }
  .canvas {
    position: relative;
    width: 1200px;
    height: 1000px;
    background: var(--canvas-grey);
  }
  .bumper-sticker {
    position: absolute;
    left: 211px;
    top: 387px;
    width: 779px;
    height: 225px;
    overflow: hidden;
    background:
      radial-gradient(ellipse 260px 140px at 370px 225px, var(--sticker-light) 0%, rgba(38,176,103,0) 100%),
      radial-gradient(ellipse 300px 160px at 420px 20px, var(--sticker-mid) 0%, rgba(10,138,69,0) 100%),
      linear-gradient(90deg, var(--sticker-deep) 0%, #076b36 30%, var(--sticker-mid) 55%, #066030 80%, var(--sticker-deep) 100%);
  }
  .slogan {
    position: absolute;
    left: 26px;
    top: 8px;
    margin: 0;
    font-family: 'Poppins', sans-serif;
    font-weight: 700;
    color: var(--text-white);
    font-size: 94px;
    line-height: 104px;
    letter-spacing: -2px;
    text-shadow: 2px 4px 6px rgba(0, 0, 0, 0.45);
  }
  .slogan-line {
    display: block;
  }
  .globe-artwork {
    position: absolute;
    left: 547px;
    top: 4px;
    width: 230px;
    height: 212px;
    border-radius: 50%;
    background:
      radial-gradient(circle at 48% 40%, var(--globe-light) 0%, #2f8a22 45%, var(--globe-dark) 78%, rgba(11,74,22,0) 80%),
      radial-gradient(circle at 50% 50%, rgba(0,0,0,0) 82%, rgba(244,210,58,0.55) 88%, rgba(244,210,58,0) 96%);
  }
</style>
</head>
<body>
  <div class="canvas">
    <div class="bumper-sticker">
      <h1 class="slogan">
        <span class="slogan-line">There is NO</span>
        <span class="slogan-line">Planet B</span>
      </h1>
      <div class="globe-artwork" role="img" aria-label="Illustration of a green Earth globe showing the Americas, framed by glowing golden rings"></div>
    </div>
  </div>
</body>
</html>
```